Copper Moth Tattoo

Business card / Appointment card in one

Ive attached the new logo along with a simple format of what I would like written out on the back! Would like a clean/ modern style font to be used! I also attached the current card for a reference of style!

The colors of this would be either white and gold lettering or black with gold lettering.

Email - CopperMothKV@inkmail-demo.com
Ph # 555-482-7319

The message at bottom of back - All cancellations or No Call No Shows within 48 hours of appointment time will result in a forfeit of deposit.

Small block avail (if card is black) to write in appointment date/time

Target Market(s)

Card for Tattoo shop

Contact Information for Business Card

in project description area!

Font styles to use
Sans Serif

Requirements
Must have
• Please refer to current business card photos that were attached as well!
Nice to have
• Looking for blacks, greys and gold for color scheme

```html
<!DOCTYPE html>
<html lang="en">
<head>
<meta charset="utf-8">
<title>Copper Moth Tattoo – Business &amp; Appointment Card</title>
<link href="https://fonts.googleapis.com/css2?family=Montserrat:wght@300;400;500&display=swap" rel="stylesheet">
<style>
  :root {
    --backdrop: #1c1c1e;
    --card-black: #141414;
    --card-white: #f3f1ec;
    --gold: #c59d67;
    --gold-soft: #d3b083;
  }
  * { box-sizing: border-box; margin: 0; padding: 0; }
  html, body {
    width: 1200px;
    height: 786px;
    overflow: hidden;
    background: var(--backdrop);
  }
  body {
    font-family: "Montserrat", sans-serif;
    font-weight: 300;
    color: var(--gold);
  }
  .stage {
    position: relative;
    width: 1200px;
    height: 786px;
  }
  .card {
    position: absolute;
    top: 238px;
    width: 540px;
    height: 309px;
    border-radius: 3px;
    box-shadow: 0 18px 40px rgba(0,0,0,0.45);
  }

  /* Appointment side */
  .card--appointment {
    left: 40px;
    background: var(--card-white);
    padding: 62px 44px 0 44px;
  }
  .appt-row {
    display: flex;
    align-items: flex-end;
    font-size: 14px;
    letter-spacing: 0.6px;
    margin-bottom: 26px;
  }
  .write-line {
    display: inline-block;
    border-bottom: 1px solid var(--gold-soft);
    height: 16px;
    margin: 0 10px 0 6px;
  }
  .write-line--long { flex: 1; }
  .write-line--short { width: 96px; margin-right: 0; }
  .weekdays {
    display: flex;
    gap: 20px;
    font-size: 14px;
    letter-spacing: 0.6px;
    margin-bottom: 22px;
  }
  .weekday { display: flex; align-items: center; gap: 7px; }
  .checkbox {
    width: 11px;
    height: 11px;
    border: 1.4px solid var(--gold);
  }
  .policy {
    font-size: 12.5px;
    line-height: 1.55;
    letter-spacing: 0.3px;
  }

  /* Contact side */
  .card--contact {
    left: 620px;
    background: linear-gradient(160deg, #1e1e1e 0%, var(--card-black) 60%, #0f0f0f 100%);
  }
  .contact-line {
    position: absolute;
    left: 42px;
    top: 62px;
    font-size: 13px;
    letter-spacing: 0.6px;
    color: var(--gold-soft);
  }
  .studio-name {
    position: absolute;
    left: 0;
    right: 0;
    top: 150px;
    text-align: center;
    font-size: 26px;
    font-weight: 400;
    letter-spacing: 5px;
    text-transform: uppercase;
    color: var(--gold);
  }
</style>
</head>
<body>
<main class="stage">

  <section class="card card--appointment" aria-label="Appointment card">
    <div class="appt-row">
      <span>Appointment on:</span>
      <span class="write-line write-line--long"></span>
      <span>Time</span>
      <span class="write-line write-line--short"></span>
    </div>
    <div class="appt-row">
      <span>Date</span>
      <span class="write-line write-line--long" style="margin-right:0"></span>
    </div>
    <div class="weekdays">
      <span class="weekday"><span class="checkbox"></span>Mon.</span>
      <span class="weekday"><span class="checkbox"></span>Tues.</span>
      <span class="weekday"><span class="checkbox"></span>Wed.</span>
      <span class="weekday"><span class="checkbox"></span>Thurs.</span>
      <span class="weekday"><span class="checkbox"></span>Fri.</span>
      <span class="weekday"><span class="checkbox"></span>Sat.</span>
    </div>
    <p class="policy">All cancellations or No Call No Shows within 48 hours of<br>Appointment time will result in a forfeit of deposit.</p>
  </section>

  <section class="card card--contact" aria-label="Business card">
    <p class="contact-line">E : CopperMothKV@inkmail-demo.com | P : 555-482-7319</p>
    <h1 class="studio-name">Copper Moth Tattoo</h1>
  </section>

</main>
</body>
</html>
```